Brightpath Orthodontics appointment card design

I need appointment cards/ business cards made. Front will be Logo, name, title, email, phone number and location (5274 Willowmere Pkwy, Ste 312, Concord, NC 28027) . the back should have an appointment card (name, time, date) and also 3 addresses listed with a check box so we can check to which location they are going.
Brent Pellman Orthodontics
- 6315 Harlow Avenue, Ste 104, Harrisburg, NC 28075
- 2947 Rosvale Court SW, Ste 500, Concord, NC 28025
- 7163 Fernbrook Corporate Parkway, Ste 404, Charlotte, NC 28277
Business card can be horizontal or vertical in Design.
I need to be able to edit it to update and add new employees

Requirements
Must have
• Front:
• - Logo
• - Name & Title (able to be edited)
• - phone (704-555-0148) & Email (need to be able to edit)
• - Address: 5274 Willowmere Pkwy, Ste 312
• Concord, NC 28027
• Back:
• Appointment Card design:
• - Name, time, Date
• - 3 locations w/ a check box so the patient knows where to go:
• Brent Pellman Orthodontics
• - 6315 Harlow Avenue, Ste 104, Harrisburg, NC 28075
• - 2947 Rosvale Court SW, Ste 500, Concord, NC 28025
• - 7163 Fernbrook Corporate Parkway, Ste 404, Charlotte, NC 28277

```html
<!DOCTYPE html>
<html lang="en">
<head>
<meta charset="utf-8">
<title>Brightpath Orthodontics – Business &amp; Appointment Card</title>
<link href="https://fonts.googleapis.com/css2?family=Lato:wght@400;700;900&family=Oswald:wght@600&display=swap" rel="stylesheet">
<style>
  :root {
    --page-bg: #2a2b2d;
    --navy-light: #1a2f4a;
    --navy-dark: #0b1422;
    --brand-blue: #2a7cc7;
    --card-grey: #e8e8e8;
    --ink: #2b2b2b;
    --white: #ffffff;
    --muted-white: #d9e2ec;
  }
  * { box-sizing: border-box; margin: 0; padding: 0; }
  html, body { width: 1200px; height: 1200px; overflow: hidden; }
  body {
    background: var(--page-bg);
    font-family: "Lato", sans-serif;
    position: relative;
  }
  .card {
    position: absolute;
    left: 150px;
    width: 900px;
    height: 514px;
    border-radius: 4px;
    overflow: hidden;
  }

  /* Front */
  .card-front {
    top: 60px;
    background: radial-gradient(ellipse at 45% 30%, var(--navy-light) 0%, var(--navy-dark) 75%);
    color: var(--white);
  }
  .front-brand {
    position: absolute;
    top: 120px; left: 0; right: 0;
    text-align: center;
    display: flex; justify-content: center; align-items: center; gap: 18px;
  }
  .brand-dot {
    width: 26px; height: 26px; border-radius: 50%;
    background: var(--brand-blue);
  }
  .brand-name {
    font-family: "Lato", sans-serif;
    font-weight: 700;
    font-size: 52px;
    color: var(--brand-blue);
    letter-spacing: 0.5px;
  }
  .front-details {
    position: absolute;
    top: 270px; left: 0; right: 0;
    display: flex; justify-content: center; align-items: center; gap: 26px;
  }
  .person { text-align: right; }
  .person-name {
    font-family: "Oswald", sans-serif;
    font-weight: 600;
    font-size: 34px;
    letter-spacing: 0.5px;
    line-height: 1.05;
  }
  .person-title { color: var(--brand-blue); font-size: 20px; }
  .divider { width: 2px; height: 84px; background: var(--brand-blue); }
  .contacts { list-style: none; font-size: 19px; color: var(--muted-white); }
  .contacts li { display: flex; align-items: center; gap: 10px; line-height: 1.45; }
  .contacts svg { width: 16px; height: 16px; fill: var(--brand-blue); flex: none; }
  .front-address {
    position: absolute;
    bottom: 60px; left: 0; right: 0;
    text-align: center;
    font-size: 21px;
    color: var(--white);
  }

  /* Back */
  .card-back {
    top: 626px;
    background: var(--card-grey);
    color: var(--ink);
  }
  .back-brand {
    position: absolute;
    top: 48px; left: 60px;
    display: flex; align-items: center; gap: 12px;
  }
  .back-brand .brand-dot { width: 18px; height: 18px; }
  .back-brand .brand-name { font-size: 32px; }
  .fields {
    position: absolute;
    top: 140px; left: 60px; right: 60px;
  }
  .field-row { display: flex; align-items: flex-end; gap: 14px; margin-bottom: 26px; }
  .field-label { font-weight: 700; font-size: 22px; white-space: nowrap; }
  .field-line { flex: 1; height: 2px; background: var(--brand-blue); margin-bottom: 6px; }
  .locations {
    position: absolute;
    top: 300px; left: 60px;
    list-style: none;
  }
  .locations li { display: flex; align-items: center; gap: 16px; font-size: 22px; line-height: 1.55; }
  .locations .practice { font-weight: 900; font-size: 23px; }
  .bullet-square { width: 16px; height: 16px; background: var(--ink); flex: none; }
  .check-box { width: 16px; height: 16px; border: 2px solid var(--brand-blue); flex: none; margin-left: 26px; }
</style>
</head>
<body>

<section class="card card-front" aria-label="Business card front">
  <div class="front-brand">
    <span class="brand-dot"></span>
    <span class="brand-name">Brightpath Orthodontics</span>
  </div>

  <div class="front-details">
    <div class="person">
      <div class="person-name">DANIEL REYES</div>
      <div class="person-title">CEO / Manager</div>
    </div>
    <div class="divider"></div>
    <ul class="contacts">
      <li>
        <svg viewBox="0 0 16 16"><path d="M3.5 1.5l2.5 0 1.2 3.2-1.6 1.2a8 8 0 0 0 4.5 4.5l1.2-1.6 3.2 1.2v2.5c0 .8-.7 1.5-1.5 1.5A12.5 12.5 0 0 1 2 3c0-.8.7-1.5 1.5-1.5z"/></svg>
        +704-555-0148
      </li>
      <li>
        <svg viewBox="0 0 16 16"><path d="M8 1a7 7 0 1 0 0 14A7 7 0 0 0 8 1zm0 2a5 5 0 1 1 0 10A5 5 0 0 1 8 3z"/><rect x="2" y="7.2" width="12" height="1.6"/><rect x="7.2" y="2" width="1.6" height="12"/></svg>
        www.brightpathortho.com
      </li>
      <li>
        <svg viewBox="0 0 16 16"><path d="M1 3h14v10H1zM2.5 4.5v.4L8 8.6l5.5-3.7v-.4z"/></svg>
        hello@brightpathortho.com
      </li>
    </ul>
  </div>

  <p class="front-address">5274 Willowmere Pkwy, Ste 312 - Concord, NC 28027</p>
</section>

<section class="card card-back" aria-label="Appointment card back">
  <div class="back-brand">
    <span class="brand-dot"></span>
    <span class="brand-name">Brightpath Orthodontics</span>
  </div>

  <div class="fields">
    <div class="field-row">
      <span class="field-label">Name :</span><span class="field-line"></span>
      <span class="field-label">Date :</span><span class="field-line"></span>
    </div>
    <div class="field-row">
      <span class="field-label">Time :</span><span class="field-line"></span>
    </div>
  </div>

  <ul class="locations">
    <li class="practice"><span class="bullet-square"></span>Brent Pellman Orthodontics :</li>
    <li><span class="check-box"></span>6315 Harlow Avenue, Ste 104, Harrisburg, NC 28075</li>
    <li><span class="check-box"></span>2947 Rosvale Court SW, Ste 500, Concord, NC 28025</li>
    <li><span class="check-box"></span>7163 Fernbrook Corporate Parkway, Ste 404, Charlotte, NC 28277</li>
  </ul>
</section>

</body>
</html>
```